Business Card Design Project

New business card design front and back for IT company that does network support and web design.
Calloway IT
Doug Calloway
Managing Director
PO Box 918 Brinsley VIC 3421
doug@callowayit.example
www.callowayit.example

Industry/Entity Type

Business

```html
<!DOCTYPE html>
<html lang="en">
<head>
<meta charset="utf-8">
<title>Calloway IT – Business Card</title>
<link rel="stylesheet" href="https://fonts.googleapis.com/css2?family=Tinos&display=swap">
<style>
  :root {
    --card-bg: #e4e4f0;
    --card-border: #a9d7ee;
    --ink: #000000;
  }
  html, body {
    margin: 0;
    padding: 0;
    width: 1200px;
    height: 686px;
    overflow: hidden;
    background: var(--card-bg);
  }
  .card {
    position: relative;
    width: 1200px;
    height: 686px;
    box-sizing: border-box;
    border: 2px solid var(--card-border);
    background: var(--card-bg);
    font-family: "Tinos", "Times New Roman", serif;
    color: var(--ink);
  }
  .line {
    position: absolute;
    left: 0;
    right: 0;
    margin: 0;
    text-align: center;
    line-height: 1;
    font-weight: 400;
    word-spacing: 0.12em;
    white-space: nowrap;
  }
  .card-name   { top: 92px;  font-size: 68px; }
  .card-role   { top: 193px; font-size: 50px; }
  .card-phone  { top: 307px; font-size: 48px; }
  .card-postal { top: 425px; font-size: 52px; }
  .card-links {
    position: absolute;
    left: 40px;
    right: 32px;
    top: 592px;
    display: flex;
    justify-content: space-between;
    font-size: 52px;
    line-height: 1;
    white-space: nowrap;
  }
</style>
</head>
<body>
  <div class="card" aria-label="Calloway IT business card">
    <h1 class="line card-name">Doug Calloway</h1>
    <p class="line card-role">Managing Director</p>
    <p class="line card-phone">0400 555 182</p>
    <p class="line card-postal">PO Box 918 Brinsley VIC 3421</p>
    <div class="card-links">
      <span class="card-email">doug@callowayit.example</span>
      <span class="card-web">www.callowayit.example</span>
    </div>
  </div>
</body>
</html>
```